Pellbrook Varnley Ltd

Fabrication of Gates ,Railings,metal staircases,gate automation and enrty systems

free estimates
free design service

all

It Service

• company logo
contact details
web address
email address

```html
<!DOCTYPE html>
<html lang="en">
<head>
<meta charset="utf-8">
<title>Pellbrook Varnley Ltd – Flyer</title>
<link href="https://fonts.googleapis.com/css2?family=Open+Sans:wght@400;600;700;800&display=swap" rel="stylesheet">
<style>
:root{
  --stage:#e9e7e3;
  --paper:#ffffff;
  --blue-deep:#3f5c8a;
  --blue-mid:#5f78a3;
  --blue-soft:#a6b3cf;
  --swoosh:#a9b5d8;
  --night:#0c0d12;
  --heading:#b9c3df;
  --body-light:#e8eaf0;
  --ink:#2b2f38;
  --brand:#3d5f93;
}
*{margin:0;padding:0;box-sizing:border-box}
html,body{width:1200px;height:899px;overflow:hidden}
body{background:var(--stage);font-family:"Open Sans",Arial,sans-serif;position:relative}
.flyer{position:absolute;left:333px;top:67px;width:574px;height:743px;background:var(--paper);overflow:hidden;box-shadow:0 2px 10px rgba(0,0,0,.18)}
.tile{position:absolute;width:150px;display:flex;flex-direction:column;align-items:center;justify-content:center;text-align:center;color:#fff}
.tile--blue{background:linear-gradient(135deg,var(--blue-deep) 0%,var(--blue-mid) 55%,var(--blue-soft) 100%)}
.tile--photo{background:var(--paper);padding:11px}
.photo{width:100%;height:100%}
.photo--gate{background:linear-gradient(180deg,#c9d7ea 0%,#8d8578 55%,#4e4a44 100%)}
.photo--rail{background:linear-gradient(160deg,#b9826a 0%,#7c6a5a 45%,#4f7a3a 100%)}
.photo--fence{background:linear-gradient(180deg,#d5dde8 0%,#9a9c9f 50%,#6b6e70 100%)}
.photo--park{background:linear-gradient(180deg,#9fb2a0 0%,#4f6e3d 55%,#8d7565 100%)}
.photo--house{background:linear-gradient(180deg,#c8c9cf 0%,#a35a4a 50%,#3a3535 100%)}
.big{font-size:37px;font-weight:800;line-height:1}
.sub{font-size:17px;font-weight:700;line-height:1.1}
.small{font-size:12px;font-weight:600}
.label{font-size:15px;font-weight:700;line-height:1.25}
.label-lg{font-size:19px;font-weight:700;line-height:1.25}
.panel{position:absolute;left:299px;top:0;width:275px;height:660px;background:var(--night)}
.panel__photo{position:absolute;left:0;top:0;width:275px;height:200px;background:radial-gradient(circle at 88% 38%,#e6edff 0%,#8fa0c8 10%,#2a3042 35%,#0c0d12 75%)}
.panel__text{position:absolute;left:51px;top:86px;width:190px;color:var(--body-light)}
.panel__heading{font-size:10.5px;font-weight:700;color:var(--heading);letter-spacing:.4px;margin-bottom:14px}
.panel__item{font-size:9.4px;font-weight:700;line-height:1.25;margin-bottom:11px}
.panel__heading--services{margin-top:30px}
.curve{position:absolute;left:0;top:0}
.contact{position:absolute;left:19px;top:644px;color:var(--ink)}
.contact__title{font-size:16px;font-weight:700;color:var(--brand);margin-bottom:7px}
.contact__lines{font-size:9.5px;font-weight:600;line-height:1.3;padding-left:3px}
.web{position:absolute;left:116px;top:711px;font-size:13.5px;font-weight:700;color:var(--brand)}
.brand{position:absolute;left:340px;top:652px;display:flex;align-items:center;gap:9px}
.brand__mark{width:26px;height:26px;background:var(--brand)}
.brand__name{font-size:22px;font-weight:700;color:var(--brand);line-height:1.05;width:180px}
</style>
</head>
<body>
<main class="flyer">
  <div class="tile tile--photo" style="left:0;top:0;height:131px"><div class="photo photo--gate" role="img" aria-label="Photo of a wrought iron driveway gate between brick pillars"></div></div>
  <div class="tile tile--blue" style="left:149px;top:0;height:131px"><span class="big">FREE</span><span class="sub">estimates</span></div>

  <div class="tile tile--blue" style="left:0;top:131px;height:124px"><span class="big">FREE</span><span class="small">design service</span></div>
  <div class="tile tile--photo" style="left:149px;top:131px;height:124px"><div class="photo photo--rail" role="img" aria-label="Photo of black metal railings on a brick wall"></div></div>

  <div class="tile tile--photo" style="left:0;top:255px;height:123px"><div class="photo photo--fence" role="img" aria-label="Photo of decorative metal fence panels along a pavement"></div></div>
  <div class="tile tile--blue" style="left:149px;top:255px;height:123px"><span class="label-lg">Gates,</span><span class="label">metal<br>staircases</span></div>

  <div class="tile tile--blue" style="left:0;top:378px;height:123px"><span class="label">gate<br>automation<br>and entry<br>systems</span></div>
  <div class="tile tile--photo" style="left:149px;top:378px;height:123px"><div class="photo photo--park" role="img" aria-label="Photo of a black metal gate beside a lawn"></div></div>

  <div class="tile tile--photo" style="left:0;top:501px;height:112px"><div class="photo photo--house" role="img" aria-label="Photo of black railings in front of brick houses"></div></div>
  <div class="tile tile--blue" style="left:149px;top:501px;height:112px"><span class="label-lg">Railings</span></div>

  <section class="panel">
    <div class="panel__photo" role="img" aria-label="Photo of a welder at work with sparks"></div>
    <div class="panel__text">
      <h2 class="panel__heading">PRODUCTS:</h2>
      <p class="panel__item">Custom Tanks including hydraulic and hydration</p>
      <p class="panel__item">Combustion Stacks</p>
      <p class="panel__item">Frac Equipment including fenders and toolboxes Coil Tubing Units / Nitrogen Pumpers Skid Packages, Stairs, Ladders, Platforms Waste Water Treatment Plant Equipment Industrial SS Fabrication / Light Structural Stainless, Aluminum, Mild Steel</p>
      <h2 class="panel__heading panel__heading--services">SERVICES:</h2>
      <p class="panel__item">Welding</p>
      <p class="panel__item">Rolling up to 1/2" plate and 8 foot wide</p>
      <p class="panel__item">Shearing – 10 foot long by 1/4" thick</p>
      <p class="panel__item">Braking – 10 foot long by 3/8" thick</p>
      <p class="panel__item">CNC Plasma Table c/w 5 Axis Bevel Head – 10' x 40' (CS/AL/SS 3" thk)</p>
      <p class="panel__item">Pipe and structural rolling</p>
      <p class="panel__item">Machine shop</p>
    </div>
  </section>

  <svg class="curve" width="574" height="743" viewBox="0 0 574 743" aria-hidden="true">
    <path d="M0,628 C170,640 430,610 574,478 L574,743 L0,743 Z" fill="#ffffff"/>
    <path d="M0,622 C170,634 430,604 574,472" fill="none" stroke="var(--swoosh)" stroke-width="8"/>
  </svg>

  <div class="contact">
    <h3 class="contact__title">Contact Us:</h3>
    <p class="contact__lines">Unit #4 - 2270 61 Ave SE<br>Calgary, AB<br>Canada T2X 4K7<br>P: 403 555-0148<br>F: 403 555.0172</p>
  </div>
  <p class="web">www.pellbrookvarnley.com</p>
  <div class="brand">
    <span class="brand__mark"></span>
    <span class="brand__name">Pellbrook Varnley Ltd</span>
  </div>
</main>
</body>
</html>
```